Healthcare IT company looking for business card design

We develop IT systems for healthcare that significantly reduces cost and improves quality.

We want a business card design that is professional and clean, and using the colors in our logo.

Target Market(s)

Doctors and decision makers in the healthcare industry

Industry/Entity Type

Healthcare

Contact Information for Business Card

It should include
Name and title, address, telephone

Tobias Vrenholt, CEO
+46 712 418257
tobias@kelvaro.se

Font styles to use
Serif

Colors
0355a3
ed282f

Requirements
Must have
• Clean design
• Professional feel
Nice to have
• N/A
Should not have
• N/A

```html
<!DOCTYPE html>
<html lang="en">
<head>
<meta charset="UTF-8">
<title>Kelvaro – Business Card</title>
<link href="https://fonts.googleapis.com/css2?family=Open+Sans:wght@400;600;700&display=swap" rel="stylesheet">
<style>
  :root {
    --brand-blue: #0355a3;
    --brand-red: #ed282f;
    --card-white: #ffffff;
    --stage: #e9ebee;
  }
  * { margin: 0; padding: 0; box-sizing: border-box; }
  html, body { width: 1200px; height: 800px; overflow: hidden; }
  body {
    background: var(--stage);
    font-family: "Open Sans", Arial, sans-serif;
    display: flex;
    align-items: center;
    justify-content: center;
    gap: 40px;
  }
  .card {
    position: relative;
    width: 540px;
    height: 310px;
    border-radius: 16px;
    overflow: hidden;
    box-shadow: 0 6px 18px rgba(0,0,0,0.12);
  }
  .card-front { background: var(--card-white); }
  .card-back { background: var(--brand-red); display: flex; align-items: center; justify-content: center; }

  .brand-name {
    position: absolute;
    left: 36px;
    top: 62px;
    font-size: 50px;
    font-weight: 700;
    color: var(--brand-blue);
    letter-spacing: -0.5px;
  }
  .divider {
    position: absolute;
    left: 292px;
    top: 52px;
    width: 2px;
    height: 170px;
    background: linear-gradient(to bottom, rgba(3,85,163,0.9), rgba(3,85,163,0));
  }
  .contact {
    position: absolute;
    left: 314px;
    top: 58px;
    color: var(--brand-blue);
    font-size: 14px;
    line-height: 1.3;
  }
  .contact .person-name { font-size: 18px; font-weight: 700; }
  .contact .person-title { font-size: 13px; margin-bottom: 16px; }
  .contact .address { margin-bottom: 10px; }
  .contact .line { display: flex; align-items: center; gap: 7px; }
  .contact svg { flex: none; }

  .bottom-band { position: absolute; left: 0; bottom: 0; width: 100%; height: 16px; }

  .back-name {
    font-size: 48px;
    font-weight: 700;
    color: var(--card-white);
    letter-spacing: -0.5px;
  }
</style>
</head>
<body>
  <section class="card card-front">
    <div class="brand-name">Kelvaro</div>
    <div class="divider"></div>
    <div class="contact">
      <div class="person-name">Tobias Vrenholt</div>
      <div class="person-title">CEO</div>
      <div class="address">123, Main Avenue, Any City,<br>NY 10001</div>
      <div class="line">
        <svg width="13" height="13" viewBox="0 0 24 24" aria-hidden="true"><path fill="#ed282f" d="M6.6 10.8a15 15 0 0 0 6.6 6.6l2.2-2.2c.3-.3.7-.4 1-.2 1.1.4 2.3.6 3.6.6.6 0 1 .4 1 1V20c0 .6-.4 1-1 1A17 17 0 0 1 3 4c0-.6.4-1 1-1h3.5c.6 0 1 .4 1 1 0 1.3.2 2.5.6 3.6.1.3 0 .7-.2 1z"/></svg>
        <span>+46 712 418257</span>
      </div>
      <div class="line">
        <svg width="14" height="11" viewBox="0 0 24 18" aria-hidden="true"><rect width="24" height="18" rx="2" fill="#ed282f"/><path d="M1 2l11 8 11-8" stroke="#fff" stroke-width="2" fill="none"/></svg>
        <span>tobias@kelvaro.se</span>
      </div>
    </div>
    <svg class="bottom-band" viewBox="0 0 540 16" preserveAspectRatio="none" aria-hidden="true">
      <polygon points="0,0 200,0 216,16 0,16" fill="#ed282f"/>
      <polygon points="200,0 540,0 540,16 216,16" fill="#0355a3"/>
    </svg>
  </section>

  <section class="card card-back">
    <div class="back-name">Kelvaro</div>
  </section>
</body>
</html>
```